Verdant Holdings SA Business Cards

Dear all,
Thank you for reading my brief and project. My company is doing doing advisory in real estate and to comapnies + real estates services as asset management, brokerage, development etc.
I would like to get a business card for my company which is clear, professionnal and serious.
Please have a look to the attachement to see the logos of the company

Industry/Entity Type

Real Estate

Contact Information for Business Card

I would like to have in the business card the following
Principal side:
- Logo of the company (or Monogram)
- First and Last Name (Marcel Tobler)
- Mobile number
- email address

Second side:
- Address (Chemin des Vergers 17, 1292 Chambésy - Switzerland)
- website (www.verdantholdings.ch)

Requirements
Must have
• Refer to the typeface and logo colors

```html
<!DOCTYPE html>
<html lang="en">
<head>
<meta charset="utf-8">
<title>Verdant Holdings SA – Business Cards</title>
<link rel="stylesheet" href="https://fonts.googleapis.com/css2?family=Lato:wght@400;700&family=Raleway:wght@500;600&display=swap">
<style>
  :root {
    --slate: #3a4556;
    --blue: #0b72c1;
    --paper: #ffffff;
    --backdrop: #cfd0d1;
    --ink: #2f3743;
  }
  * { box-sizing: border-box; margin: 0; padding: 0; }
  html, body { width: 1200px; height: 802px; overflow: hidden; }
  body { background: var(--backdrop); position: relative; font-family: "Lato", sans-serif; }

  .card {
    position: absolute;
    top: 274px;
    width: 443px;
    height: 264px;
    background: var(--paper);
    box-shadow: 2px 3px 5px rgba(0,0,0,0.35);
    overflow: hidden;
  }
  .card--front { left: 136px; }
  .card--back { left: 624px; }

  /* Front */
  .front-band {
    position: absolute; left: 0; top: 0; width: 100%; height: 80px;
    background: linear-gradient(to right, var(--slate) 0 352px, var(--blue) 352px 100%);
  }
  .front-wordmark {
    position: absolute; left: 33px; top: 34px;
    font-family: "Raleway", sans-serif; font-weight: 600;
    font-size: 23px; letter-spacing: 0.4px; line-height: 1;
    color: var(--blue); text-transform: uppercase;
  }
  .front-dot {
    position: absolute; left: 318px; top: 8px;
    width: 76px; height: 76px; border-radius: 50%;
    background: var(--paper);
  }
  .person-name {
    position: absolute; left: 33px; top: 153px;
    font-size: 16px; line-height: 1; letter-spacing: 0.2px; text-transform: uppercase;
  }
  .person-name .first { color: var(--slate); font-weight: 700; }
  .person-name .last { color: var(--blue); font-weight: 400; }
  .contact-list { position: absolute; left: 34px; top: 192px; list-style: none; }
  .contact-list li {
    display: flex; align-items: center; gap: 4px;
    font-size: 13px; line-height: 16.5px; color: var(--ink);
  }
  .contact-list svg { width: 11px; height: 11px; fill: var(--blue); }

  /* Back */
  .back-dot {
    position: absolute; left: 77px; top: 84px;
    width: 56px; height: 56px; border-radius: 50%;
    background: var(--slate);
  }
  .back-divider {
    position: absolute; left: 164px; top: 71px;
    width: 1.5px; height: 81px; background: var(--blue);
  }
  .back-wordmark {
    position: absolute; left: 190px; top: 103px;
    font-family: "Raleway", sans-serif; font-weight: 600;
    font-size: 20px; letter-spacing: 0.3px; line-height: 1;
    color: var(--slate); text-transform: uppercase;
  }
  .address-band {
    position: absolute; left: 0; top: 176px; width: 100%; height: 33px;
    background: var(--blue); color: var(--paper);
    display: flex; align-items: center; justify-content: center;
    font-size: 12.5px; letter-spacing: -0.1px;
  }
  .website {
    position: absolute; left: 0; top: 225px; width: 100%;
    text-align: center; font-size: 12px; line-height: 14px;
    color: var(--blue); text-transform: uppercase;
  }
</style>
</head>
<body>
  <section class="card card--front" aria-label="Business card, front">
    <div class="front-band"></div>
    <div class="front-dot"></div>
    <p class="front-wordmark">Verdant Holdings</p>
    <p class="person-name"><span class="first">Marcel</span> <span class="last">Tobler</span></p>
    <ul class="contact-list">
      <li>
        <svg viewBox="0 0 12 12" aria-hidden="true"><path d="M1 4.2C1 2.6 3.2 1.6 6 1.6s5 1 5 2.6v.9H8.6V3.9H3.4v1.2H1z M3.2 5.6h5.6l1.6 4.8H1.6z"/></svg>
        022-587 310 446
      </li>
      <li>
        <svg viewBox="0 0 12 12" aria-hidden="true"><path d="M1 2.5h10v7H1z M1.6 3.1 6 6.6l4.4-3.5" fill="var(--blue)" stroke="#fff" stroke-width="0.8"/></svg>
        contact@verdantholdings.ch
      </li>
    </ul>
  </section>

  <section class="card card--back" aria-label="Business card, back">
    <div class="back-dot"></div>
    <div class="back-divider"></div>
    <p class="back-wordmark">Verdant Holdings</p>
    <p class="address-band">Chemin des Vergers 17, 1292 Chambésy - Switzerland</p>
    <p class="website">www.verdantholdings.ch</p>
  </section>
</body>
</html>
```